Redesign our pitch deck

Hi! We want to redesign the attached pitch deck (the PITCH DECK TO REDESIGN PPT-file) according to styles, graphics and fonts in our brand book.

Link to the brandbook zipfile with all design files HERE:
https://files.morvexa.net/share/d/8qWz3Lp0vKd2Rt7YbXnA4eJmQs5hUo/view?usp=sharing

A few general pointers
1: All the graphs (excel-grids etc) for our current pitch deck can be redesigned however you like, but should maintain their general structure so we can simply add the numbers.

2: Images/graphics on some slides would be good as long as they follow the brandbooks graphical style and fit the headline for the slide. The screens in the brandbook can also be used where they would fit in.

3: As for the rest of the slides design them in the best possible way, while following our brandbook and leaving ample room to add text.

If you have any questions and need anything else i will try to provide it, just contact me via pixelbazaar.

Thanks and good luck
/Leonhardt

Target Market(s)

Investor pitch

Industry/Entity Type

Gaming

Requirements
Nice to have
• All is in the brief

```html
<!DOCTYPE html>
<html lang="en">
<head>
<meta charset="utf-8">
<title>quizora — Pitch Deck</title>
<link href="https://fonts.googleapis.com/css2?family=Encode+Sans+Semi+Condensed:wght@400;500&family=Roboto:wght@400;500;700&display=swap" rel="stylesheet">
<style>
:root{
  --page:#f3f6fb;
  --slide:#ffffff;
  --navy:#2a3352;
  --ink:#3b4256;
  --muted:#8a93a8;
  --pink:#ef5f8a;
  --blue:#2f7ff0;
  --purple:#9b6ee8;
  --sky:#3aa0f0;
  --cyan:#22c9f0;
  --teal:#0a7c8a;
  --green:#5cc95a;
}
*{box-sizing:border-box;margin:0;padding:0}
html,body{width:1200px;height:3078px;overflow:hidden;background:var(--page)}
body{position:relative;font-family:"Roboto",sans-serif;color:var(--ink)}
.slide{position:absolute;left:135px;width:874px;height:491px;background:var(--slide);overflow:hidden;box-shadow:0 28px 40px -18px rgba(60,80,130,.22)}
.abs{position:absolute}
.heading{font-family:"Encode Sans Semi Condensed",sans-serif;font-weight:400;color:var(--navy);letter-spacing:-1px;white-space:nowrap}
.accent-bar{position:absolute;height:3px;width:76px;background:var(--pink);border-radius:2px}
.brand{position:absolute;display:flex;align-items:center;gap:8px;font-family:"Roboto",sans-serif;font-weight:700;color:var(--navy)}
.brand .dot{border-radius:50%;background:var(--blue)}
.brand-sm{left:32px;top:23px;font-size:20px}
.brand-sm .dot{width:16px;height:16px}
.footer{position:absolute;right:36px;bottom:18px;font-size:10px;color:var(--navy)}
.footer b{color:var(--blue);font-weight:500;margin-right:4px}
.body-text{font-size:12px;line-height:20px;color:var(--ink)}
.art{position:absolute}

/* cover */
.cover{top:133px;background:linear-gradient(160deg,#d2e5fc 0%,#d7e3fb 50%,#e3d9f8 100%)}
.cover .brand{left:0;right:0;justify-content:center;top:74px;font-size:38px;gap:12px}
.cover .brand .dot{width:24px;height:24px}
.cover-title{left:0;right:0;text-align:center;top:202px;font-size:39px}
.cover-sub{left:0;right:0;text-align:center;top:256px;font-size:26px;color:#8c95b0;letter-spacing:-.8px}
.cover-name{left:0;right:0;text-align:center;top:323px;font-size:25px;color:var(--teal);letter-spacing:-1.2px}
.cover-dot{left:537px;top:393px;width:14px;height:14px;border-radius:50%;background:#9cc3f2}
.cover-date{left:73px;top:449px;font-size:16px;color:#4b5470}
.cover-web{left:695px;top:450px;font-size:16px;color:#4b5470}

/* who we are */
.who{top:703px}
.who-title{left:0;right:0;text-align:center;top:76px;font-size:39px}
.pillar{position:absolute;top:158px;width:200px;text-align:center}
.pillar .art{position:relative;margin:0 auto;width:130px;height:130px;border-radius:50%}
.pillar h3{margin-top:32px;font-size:12px;font-weight:500;color:var(--navy)}
.pillar p{margin-top:12px;font-size:10px;line-height:17px;color:var(--ink)}

/* why */
.why{top:1274px}
.why-title{left:439px;top:108px;font-size:49px}

/* solution */
.solution{top:1845px}
.sol-title{left:87px;top:96px;font-size:52px}
.step{position:absolute;left:106px;display:flex;align-items:center}
.step .num{width:102px;font-family:"Encode Sans Semi Condensed",sans-serif;font-size:50px;line-height:1}
.step p{font-size:17px;line-height:25px;color:var(--ink)}
.phone{position:absolute;background:#fff;border-radius:14px;box-shadow:0 10px 30px rgba(60,80,130,.16);font-size:6px;color:var(--navy);padding:8px 10px;overflow:hidden}
.phone .bar{display:flex;justify-content:space-between;font-size:5px;font-weight:700}
.phone .ttl{font-weight:700;font-size:9px;margin-top:14px}
.phone .hello{font-weight:700;font-size:13px;line-height:15px;margin-top:10px}
.phone .card{margin-top:10px;height:58px;border-radius:8px;background:linear-gradient(120deg,#8a6df0,#b18cf7);color:#fff;font-weight:700;font-size:8px;padding:8px;position:relative}
.phone .row{display:flex;justify-content:space-between;margin-top:12px;font-weight:700;font-size:6px}
.phone .row span:last-child{color:var(--blue);font-weight:400;font-size:5px}
.chips{display:flex;justify-content:space-between;margin-top:8px}
.chip{width:24px;text-align:center;font-size:4.5px}
.chip i{display:block;width:20px;height:20px;border-radius:6px;margin:0 auto 4px}
.tabbar{position:absolute;left:10px;right:10px;bottom:8px;display:flex;justify-content:space-between}
.tabbar i{width:7px;height:7px;border-radius:2px;border:1px solid #b7bfd1}
.tabbar i.on{background:var(--blue);border-color:var(--blue)}
.subj{display:flex;align-items:center;gap:6px;margin-top:14px}
.subj i{width:18px;height:18px;border-radius:5px;flex:none}
.subj div{flex:1;font-size:6px;font-weight:700;line-height:7px}
.subj small{display:block;font-weight:400;font-size:4px;color:var(--muted)}
.ring{width:22px;height:22px;border-radius:50%;border:2px solid;font-size:6px;font-weight:700;display:flex;align-items:center;justify-content:center}

/* market */
.market{top:2415px}
.market-photo{left:0;top:0;width:874px;height:200px}
.badge{left:78px;top:98px;width:172px;height:172px;border-radius:50%;background:linear-gradient(180deg,#55d8f7,#14b8e8);box-shadow:0 14px 26px rgba(20,150,200,.3);color:#fff;text-align:center;font-weight:700;font-size:12px;line-height:22px;padding-top:36px}
.badge svg{display:block;margin:0 auto 10px}
.mk-title{left:277px;top:199px;font-size:52px;line-height:64px}
.mk-title .hl{color:var(--cyan)}
.mk-lead{left:558px;top:205px;font-size:17px;line-height:25px;color:var(--navy)}
.mk-body{left:558px;top:266px}
.stat{position:absolute;top:350px}
.stat .pct{font-family:"Encode Sans Semi Condensed",sans-serif;font-size:42px;line-height:46px}
.stat p{font-size:12px;line-height:20px;margin-top:2px}
</style>
</head>
<body>

<!-- Slide 1: cover -->
<section class="slide cover">
  <div class="brand"><span class="dot"></span>quizora.</div>
  <h1 class="abs heading cover-title">Presentation Title Goes Here</h1>
  <p class="abs heading cover-sub">Credential Subtitle Goes Here</p>
  <p class="abs heading cover-name">Mara Ellison</p>
  <span class="abs cover-dot"></span>
  <p class="abs cover-date">June 2023</p>
  <p class="abs cover-web">website.com</p>
  <div class="art" role="img" aria-label="3D potted plant with teal leaves in a white pot" style="left:701px;top:315px;width:126px;height:134px;border-radius:40px 40px 20px 20px;background:linear-gradient(180deg,#8fd8e6 0%,#cfe0f2 60%,#e8edf6 100%)"></div>
</section>

<!-- Slide 2: who we are -->
<section class="slide who">
  <div class="brand brand-sm"><span class="dot"></span>quizora.</div>
  <span class="accent-bar" style="left:399px;top:68px"></span>
  <h2 class="abs heading who-title">Who We Are</h2>
  <div class="pillar" style="left:119px">
    <div class="art" role="img" aria-label="3D girl reading among stacks of books" style="background:linear-gradient(160deg,#a9dcf7,#d6eefb)"></div>
    <h3>Our Vision</h3>
    <p>Lorem ipsum dolor sit amet,<br>consectetur adipiscing elit, sed do<br>eiusmod tempor incididunt ut<br>labore et dolor aliqua.</p>
  </div>
  <div class="pillar" style="left:336px">
    <div class="art" role="img" aria-label="3D girl working on a laptop at a desk" style="background:linear-gradient(160deg,#c9ddf8,#e6eefb)"></div>
    <h3>Our Story</h3>
    <p>Lorem ipsum dolor sit amet,<br>consectetur adipiscing elit, sed do<br>eiusmod tempor incididunt ut<br>labore et dolor aliqua.</p>
  </div>
  <div class="pillar" style="left:554px">
    <div class="art" role="img" aria-label="3D girl meditating with a big thought swirl" style="background:linear-gradient(160deg,#c6efcf,#e5f7e8)"></div>
    <h3>Our Mission</h3>
    <p>Lorem ipsum dolor sit amet,<br>consectetur adipiscing elit, sed do<br>eiusmod tempor incididunt ut<br>labore et dolor aliqua.</p>
  </div>
  <p class="footer"><b>2</b>|&nbsp; website.com</p>
</section>

<!-- Slide 3: why we exist -->
<section class="slide why">
  <div class="brand brand-sm"><span class="dot"></span>quizora.</div>
  <div class="art" role="img" aria-label="3D desktop computer with bar chart, chat bubbles, rocket, plant and hand cursor" style="left:50px;top:98px;width:436px;height:323px;border-radius:30px;background:linear-gradient(135deg,#d7f5ea 0%,#fde1e7 45%,#dfe8fb 100%)"></div>
  <span class="accent-bar" style="left:439px;top:89px"></span>
  <h2 class="abs heading why-title">Why We Exist</h2>
  <p class="abs body-text" style="left:534px;top:270px">Lorem ipsum dolor sit amet, consectetur<br>adipiscing elit. Integer nec odio. Praesent<br>libero. Sed cursus ante dapibus diam. Sed nisi.</p>
  <p class="footer"><b>3</b>|&nbsp; website.com</p>
</section>

<!-- Slide 4: our solution -->
<section class="slide solution">
  <div class="brand brand-sm"><span class="dot"></span>quizora.</div>
  <span class="accent-bar" style="left:90px;top:85px"></span>
  <h2 class="abs heading sol-title">Our Solution</h2>
  <div class="step" style="top:194px"><span class="num" style="color:var(--purple)">01</span><p>Lorem ipsum dolor sit<br>amet, consectetur adipiscin</p></div>
  <div class="step" style="top:289px"><span class="num" style="color:var(--sky)">02</span><p>Lorem ipsum dolor sit<br>amet, consectetur adipiscin</p></div>
  <div class="step" style="top:384px"><span class="num" style="color:var(--cyan)">03</span><p>Lorem ipsum dolor sit<br>amet, consectetur adipiscin</p></div>

  <div class="phone" style="left:456px;top:91px;width:150px;height:320px">
    <div class="bar"><span>9:41</span><span>●●●</span></div>
    <p class="ttl">My Quests</p>
    <p class="hello">Hello<br>Theo!</p>
    <div class="card">Chemistry final<br>exams<div style="font-size:5px;font-weight:400;margin-top:6px">40 minutes</div>
      <div class="art" role="img" aria-label="3D microscope" style="right:6px;top:-14px;width:36px;height:66px;border-radius:10px;background:linear-gradient(180deg,#c8d2fb,#7b8cf0)"></div>
    </div>
    <div class="row"><span>Quests</span><span>See all</span></div>
    <p style="font-size:4px;color:var(--muted)">High School · Grade 12</p>
    <div class="chips">
      <span class="chip"><i style="background:#e3e6fd"></i>Physics</span>
      <span class="chip"><i style="background:#fde9d6"></i>Science</span>
      <span class="chip"><i style="background:#fde1ea"></i>Chemistry</span>
      <span class="chip"><i style="background:#dfeafd"></i>Biology</span>
    </div>
    <div class="row"><span>Video Course</span><span>See all</span></div>
    <div style="display:flex;gap:6px;margin-top:6px">
      <div role="img" aria-label="Course presenter photo" style="width:48px;height:30px;border-radius:6px;background:linear-gradient(135deg,#f4c9b7,#e9b8d8)"></div>
      <div style="font-size:5px;line-height:7px"><span style="color:#f2a93b">★ 4.6</span><br><b>Science</b><br><span style="color:var(--muted);font-size:4px">By Anna Reed</span></div>
    </div>
    <div class="tabbar"><i class="on"></i><i></i><i></i><i></i><i></i></div>
  </div>

  <div class="phone" style="left:630px;top:121px;width:149px;height:319px">
    <div class="bar"><span>9:41</span><span>●●●</span></div>
    <p class="ttl">Subjects</p>
    <div class="art" role="img" aria-label="3D purple mug with steam" style="left:48px;top:52px;width:52px;height:66px;border-radius:12px;background:linear-gradient(180deg,#fbd8d4,#a7b3f6)"></div>
    <div style="display:flex;justify-content:space-between;margin-top:110px;font-size:4.5px;color:var(--muted)"><span>Available</span><span>In Progress</span><span style="background:#eef0f6;color:var(--navy);padding:2px 6px;border-radius:6px">Passed</span></div>
    <div class="subj"><i style="background:#e3e6fd"></i><div>Physics<small>You have completed 28/36 questions</small></div><span class="ring" style="border-color:#5f86f2;color:#5f86f2">85</span></div>
    <div class="subj"><i style="background:#fde9d6"></i><div>Science<small>You have completed 22/30 questions</small></div><span class="ring" style="border-color:#5f86f2;color:#5f86f2">75</span></div>
    <div class="subj"><i style="background:#fde1ea"></i><div>Chemistry<small>You have completed 10/36 questions</small></div><span class="ring" style="border-color:#ef6b6b;color:#ef6b6b">30</span></div>
    <div class="tabbar"><i></i><i class="on"></i><i></i><i></i><i></i></div>
  </div>
  <p class="footer"><b>4</b>|&nbsp; website.com</p>
</section>

<!-- Slide 5: market & community -->
<section class="slide market">
  <svg class="art market-photo" viewBox="0 0 874 200" role="img" aria-label="Photo of hands sketching plans with a pencil beside a laptop">
    <defs><linearGradient id="photoTone" x1="0" y1="0" x2="1" y2="1"><stop offset="0" stop-color="#5c6f7d"/><stop offset=".55" stop-color="#9fb0b5"/><stop offset="1" stop-color="#d7dcd6"/></linearGradient></defs>
    <path d="M0 0H874V94C640 120 360 150 0 197Z" fill="url(#photoTone)"/>
  </svg>
  <svg class="abs" style="left:109px;top:270px" width="60" height="116" viewBox="0 0 60 116">
    <path d="M55 0V44H2V98" fill="none" stroke="#7a8499" stroke-width="1" stroke-dasharray="3 3"/>
    <circle cx="2" cy="106" r="9" fill="var(--green)" opacity=".35"/>
  </svg>
  <span class="abs" style="left:98px;top:370px;width:18px;height:18px;border-radius:50%;background:var(--green);border:3px solid #c7ecc5"></span>
  <div class="abs badge">
    <svg width="36" height="42" viewBox="0 0 36 42"><rect x="2" y="2" width="32" height="38" rx="3" fill="none" stroke="#fff" stroke-width="2.5"/><text x="18" y="22" text-anchor="middle" fill="#fff" font-family="Roboto,sans-serif" font-size="13" font-weight="700">Aa</text><line x1="8" y1="29" x2="28" y2="29" stroke="#fff" stroke-width="2"/><line x1="8" y1="34" x2="22" y2="34" stroke="#fff" stroke-width="2"/></svg>
    Lorem ipsum dolor sit<br>amet
  </div>
  <span class="accent-bar" style="left:277px;top:181px"></span>
  <h2 class="abs heading mk-title">Market &amp;<br><span class="hl">Community.</span></h2>
  <p class="abs mk-lead">Lorem ipsum dolor sit amet,<br>consectetur adipiscing elit.</p>
  <p class="abs body-text mk-body">Lorem ipsum dolor sit amet, consectetur<br>adipiscing elit. Integer nec odio. Praesent<br>libero. Sed cursus ante dapibus diam. Sed nisi.</p>
  <div class="stat" style="left:139px"><p class="pct" style="color:var(--green)">72%</p><p>Lorem ipsum dolor sit amet, consectetur<br>adipiscing elit.</p></div>
  <div class="stat" style="left:558px"><p class="pct" style="color:var(--sky)">45%</p><p>Lorem ipsum dolor sit amet, consectetur<br>adipiscing elit.</p></div>
  <p class="footer"><b>5</b>|&nbsp; website.com</p>
</section>

</body>
</html>
```